my company wok in garbage trucks
we need for each truck flyer

 i didn't find what i want .
so this project changed to profile to products
i upload pdf file
i need redisgn it. i have alot of product each one need flyer for it

Reason: 100 $

Companies , Municipalities

It Company

• see quandel site and vome and dusp
i want desing like quandel very simple and new idea . have unique identity

new idea in like button and dislike and other buttons
• evey icon at website Expressive content
font to use at all site
good font

```html
<!DOCTYPE html>
<html lang="en">
<head>
<meta charset="utf-8">
<title>pollnest – Add new poll</title>
<link rel="stylesheet" href="https://fonts.googleapis.com/css2?family=Ubuntu:wght@400;500&family=Open+Sans:wght@400&display=swap">
<style>
  :root {
    --brand-blue: #1b8fd0;
    --brand-green: #8cc63f;
    --text-label: #555555;
    --text-hint: #8a8a8a;
    --header-bg: #ffffff;
    --modal-bg: #ffffff;
    --divider: #ececec;
    --input-border: #d0d0d0;
    --button-top: #2aa9ea;
    --button-bottom: #0e8ad0;
    --button-border: #0b7fc0;
    --signout-top: #f6f6f6;
    --signout-bottom: #e2e2e2;
    --signout-border: #cfcfcf;
    --signout-text: #5e5e5e;
    --footer-bg: #a7c4d4;
    --footer-text: #2c3a44;
    --close-grey: #b5b5b5;
  }
  * { box-sizing: border-box; margin: 0; padding: 0; }
  html, body { width: 1200px; height: 792px; overflow: hidden; }
  body { position: relative; font-family: "Ubuntu", sans-serif; background: #333; }

  .site-header {
    position: absolute; left: 0; top: 0; width: 1200px; height: 81px;
    background: var(--header-bg);
  }
  .brand {
    position: absolute; left: 141px; top: 15px;
    display: flex; align-items: center; gap: 8px;
  }
  .brand-dot { width: 26px; height: 26px; border-radius: 50%; background: var(--brand-green); }
  .brand-name {
    font-family: "Ubuntu", sans-serif; font-weight: 500; font-size: 36px;
    color: var(--brand-blue); letter-spacing: -0.5px; line-height: 1;
  }
  .signout-button {
    position: absolute; left: 970px; top: 23px; width: 89px; height: 34px;
    border: 1px solid var(--signout-border); border-radius: 3px;
    background: linear-gradient(var(--signout-top), var(--signout-bottom));
    font-size: 15px; color: var(--signout-text);
    display: flex; align-items: center; justify-content: center;
  }

  .hero-backdrop {
    position: absolute; left: 0; top: 81px; width: 1200px; height: 657px;
    background:
      radial-gradient(ellipse at 15% 20%, rgba(150,60,100,0.55), transparent 40%),
      radial-gradient(ellipse at 80% 25%, rgba(170,150,60,0.45), transparent 40%),
      radial-gradient(ellipse at 10% 70%, rgba(60,120,140,0.45), transparent 40%),
      radial-gradient(ellipse at 90% 70%, rgba(120,90,60,0.45), transparent 40%),
      linear-gradient(#3e3a3e, #2e2f33);
  }

  .poll-modal {
    position: absolute; left: 170px; top: 150px; width: 860px; height: 483px;
    background: var(--modal-bg); border-radius: 4px;
  }
  .modal-close { position: absolute; right: 9px; top: 9px; width: 18px; height: 18px; }
  .modal-title {
    height: 81px; border-bottom: 1px solid var(--divider);
    text-align: center; font-weight: 500; font-size: 30px; line-height: 80px;
    color: var(--brand-blue);
  }
  .answer-row { position: absolute; left: 39px; display: flex; align-items: center; height: 39px; }
  .answer-label { width: 195px; font-size: 15px; font-weight: 400; color: var(--text-label); }
  .answer-input {
    width: 589px; height: 39px; border: 1px solid var(--input-border);
    box-shadow: inset 0 1px 2px rgba(0,0,0,0.08), 0 1px 2px rgba(0,0,0,0.06); background: #fff;
  }
  .row-1 { top: 111px; } .row-2 { top: 171px; } .row-3 { top: 231px; } .row-4 { top: 291px; }
  .poll-hint {
    position: absolute; left: 234px; top: 345px;
    font-size: 13.5px; color: var(--text-hint);
  }
  .modal-actions { position: absolute; left: 618px; top: 387px; display: flex; gap: 12px; }
  .action-button {
    width: 97px; height: 31px; border: 1px solid var(--button-border); border-radius: 2px;
    background: linear-gradient(var(--button-top), var(--button-bottom));
    color: #fff; font-size: 16px; font-weight: 500;
    display: flex; align-items: center; justify-content: center;
  }

  .site-footer {
    position: absolute; left: 0; top: 738px; width: 1200px; height: 54px;
    background: var(--footer-bg); border-top: 1px solid #c8d9e2;
    font-family: "Open Sans", sans-serif; font-size: 13.5px; color: var(--footer-text);
  }
  .footer-links { position: absolute; left: 141px; top: 17px; }
  .footer-links .sep { margin: 0 9px; }
  .footer-copyright { position: absolute; right: 141px; top: 17px; }
</style>
</head>
<body>
  <header class="site-header">
    <div class="brand">
      <span class="brand-dot"></span>
      <span class="brand-name">pollnest</span>
    </div>
    <div class="signout-button">Sign out</div>
  </header>

  <div class="hero-backdrop" role="img" aria-label="Blurred collage of poll cover images"></div>

  <section class="poll-modal">
    <svg class="modal-close" viewBox="0 0 18 18" aria-label="Close">
      <circle cx="9" cy="9" r="9" fill="var(--close-grey)"/>
      <path d="M5.5 5.5 L12.5 12.5 M12.5 5.5 L5.5 12.5" stroke="#fff" stroke-width="2" stroke-linecap="round"/>
    </svg>
    <h1 class="modal-title">Add new poll</h1>

    <div class="answer-row row-1"><span class="answer-label">Answers Text Number 1:</span><div class="answer-input"></div></div>
    <div class="answer-row row-2"><span class="answer-label">Answers Text Number 2:</span><div class="answer-input"></div></div>
    <div class="answer-row row-3"><span class="answer-label">Answers Text Number 3:</span><div class="answer-input"></div></div>
    <div class="answer-row row-4"><span class="answer-label">Answers Text Number 4:</span><div class="answer-input"></div></div>

    <p class="poll-hint">Check in place when poll - Check box if you want voters put new answer or not</p>

    <div class="modal-actions">
      <div class="action-button">Back</div>
      <div class="action-button">Next</div>
    </div>
  </section>

  <footer class="site-footer">
    <div class="footer-links">About<span class="sep">|</span>Support<span class="sep">|</span>Term<span class="sep">|</span>Privacy</div>
    <div class="footer-copyright">© Copyright pollnest 2014. | All rights reserved.</div>
  </footer>
</body>
</html>
```